Advertisement Design Project

I would like to have some advertisement ideas to promote my business. Our company provides credit repair, tax preparation, notary service, ledger preparation (for small businesses and independent contractors) tax restoration (help people with liens, levy, garnishments, etc. by negotiating with the DQV in these matters)

The name of our company is Tamberly Financing
Our "Jubilatrix" program focuses on tax preparation, restoration, and credit repair.
Our "Maple Step" program prepares ledgers for small business and independent contractors by preparing monthly ledgers so that at tax season they are not having to look everywhere for their receipts in order to get all deductions due to them during the tax season.

We need something that is catchy and will gain attention

attached is our logo. Our slogan is "Happiness, Restored!"

Thank you!

Target Market(s)

The financially distressed
Small business owners
Independent contractors
businesses that rely on credit worthy clients to do business with

Industry/Entity Type

Small Business

Requirements
Must have
• great pictures
nice layout

```html
<!DOCTYPE html>
<html lang="en">
<head>
<meta charset="utf-8">
<title>Tamberly Financing – Flyer</title>
<link rel="stylesheet" href="https://fonts.googleapis.com/css2?family=Open+Sans:wght@400;600&display=swap">
<style>
  :root {
    --ink: #1b1b1b;
    --muted: #4a4a4a;
    --title-blue: #2a86c4;
    --band-blue: #1f6fb5;
    --sky: #5cbbe0;
    --navy: #1f3a5f;
    --charcoal: #111111;
    --paper: #ffffff;
    --frame: #d9e3ee;
  }
  * { margin: 0; padding: 0; box-sizing: border-box; }
  html, body { width: 1200px; height: 888px; overflow: hidden; background: var(--paper); }
  body { font-family: "Open Sans", sans-serif; color: var(--ink); }

  .flyer { position: relative; width: 1200px; height: 888px; overflow: hidden; background: var(--paper); }
  .flyer-shapes { position: absolute; inset: 0; width: 1200px; height: 888px; }

  .brand-title {
    position: absolute; left: 412px; top: 30px;
    font-size: 54px; font-weight: 400; color: var(--title-blue);
    text-shadow: 3px 4px 6px rgba(0,0,0,0.25);
    white-space: nowrap; line-height: 1.2;
  }
  .brand-slogan {
    position: absolute; left: 414px; top: 100px;
    font-size: 29px; color: var(--muted);
    text-shadow: 2px 3px 5px rgba(0,0,0,0.2);
  }

  .brand-badge {
    position: absolute; left: 998px; top: 20px; width: 173px; height: 173px;
    background: var(--navy); border: 4px solid var(--frame);
    display: flex; align-items: center; justify-content: center; text-align: center;
    color: var(--paper); font-size: 21px; line-height: 1.2; padding: 12px;
  }

  .program { position: absolute; left: 313px; top: 236px; }
  .program-title { font-size: 33px; font-weight: 400; line-height: 44px; text-shadow: 2px 3px 5px rgba(0,0,0,0.2); }
  .program-list { list-style: none; font-size: 27px; line-height: 37px; }

  .services { position: absolute; left: 742px; top: 210px; }
  .services-title { font-size: 48px; font-weight: 400; line-height: 62px; text-shadow: 3px 4px 6px rgba(0,0,0,0.25); }
  .services-list { list-style: none; font-size: 27px; line-height: 37px; }

  .program-ledger { position: absolute; left: 742px; top: 582px; }
  .program-ledger .program-title { font-size: 27px; line-height: 37px; }
  .program-ledger .program-list { font-size: 22px; line-height: 30px; }

  .photo { position: absolute; }
  .photo-tax { left: 0; top: 344px; width: 289px; height: 184px;
    background: linear-gradient(135deg, #cfd8c8 0%, #f1efe4 50%, #f5ecb8 75%, #dcdad3 100%); }
  .photo-growth { left: 0; top: 536px; width: 289px; height: 186px;
    background: linear-gradient(160deg, #ffffff 0%, #e8f4f8 55%, #bfe2ec 100%); }
  .photo-meeting { left: 299px; top: 410px; width: 402px; height: 272px;
    background: linear-gradient(120deg, #f3f4f6 0%, #e3e7ec 45%, #aab4c4 80%, #6f7c93 100%);
    border: 2px solid var(--paper); }
  .photo-notary { left: 571px; top: 664px; width: 439px; height: 162px;
    background: linear-gradient(100deg, #9aa3ac 0%, #c9d0d7 45%, #eef1f3 70%, #7d8797 100%); }

  .contact { position: absolute; left: 161px; top: 742px; color: var(--paper); }
  .contact-label { font-size: 22px; letter-spacing: 0.5px; }
  .contact-details { list-style: none; font-size: 17px; line-height: 26px; margin-top: 6px; }
</style>
</head>
<body>
<main class="flyer">
  <svg class="flyer-shapes" viewBox="0 0 582 437" preserveAspectRatio="none" aria-hidden="true">
    <defs>
      <linearGradient id="corner-dark" x1="0" y1="0" x2="1" y2="1">
        <stop offset="0" stop-color="#0d0d0d"/>
        <stop offset="1" stop-color="#8a8a8a"/>
      </linearGradient>
      <linearGradient id="footer-dark" x1="0" y1="0" x2="1" y2="0">
        <stop offset="0" stop-color="#3a3a3a"/>
        <stop offset="0.5" stop-color="#9a9a9a"/>
        <stop offset="1" stop-color="#1a1a1a"/>
      </linearGradient>
      <linearGradient id="sweep-sky" x1="0" y1="1" x2="1" y2="0">
        <stop offset="0" stop-color="#3aa6d2"/>
        <stop offset="1" stop-color="#bfe8f5"/>
      </linearGradient>
    </defs>
    <path d="M0,0 H215 C120,22 35,80 0,172 Z" fill="url(#corner-dark)"/>
    <path d="M238,0 C140,20 40,82 0,182" fill="none" stroke="var(--sky)" stroke-width="9"/>
    <path d="M0,372 C90,350 200,352 290,395 C330,415 360,437 380,437 H0 Z" fill="url(#footer-dark)"/>
    <path d="M0,372 C90,350 200,352 290,395 C330,415 360,437 380,437" fill="none" stroke="var(--band-blue)" stroke-width="4"/>
    <path d="M582,255 C570,350 480,420 330,437 H582 Z" fill="var(--charcoal)"/>
    <path d="M582,232 C575,338 490,418 300,437 H345 C500,426 572,362 582,282 Z" fill="url(#sweep-sky)"/>
  </svg>

  <div class="photo photo-tax" role="img" aria-label="Photo of banknotes, a calculator and a tax time note on a spreadsheet"></div>
  <div class="photo photo-growth" role="img" aria-label="Illustration of a figure pushing a large dollar sign"></div>
  <div class="photo photo-meeting" role="img" aria-label="Photo of a couple shaking hands with a financial advisor"></div>
  <div class="photo photo-notary" role="img" aria-label="Photo of a hand stamping a document beside a laptop and phone"></div>

  <h1 class="brand-title">Tamberly Financing</h1>
  <p class="brand-slogan">Happiness, Restored!</p>

  <div class="brand-badge">Tamberly Financing</div>

  <section class="program">
    <h2 class="program-title">"Jubilatrix" program</h2>
    <ul class="program-list">
      <li>Tax preparation</li>
      <li>Restoration</li>
      <li>and credit repair.</li>
    </ul>
  </section>

  <section class="services">
    <h2 class="services-title">Company provides</h2>
    <ul class="services-list">
      <li>credit repair</li>
      <li>tax preparation</li>
      <li>notary service</li>
      <li>ledger preparation</li>
      <li>tax restoration (help people<br>with liens, levy, garnishments, etc.<br>by negotiating with the DQV in<br>these matters)</li>
    </ul>
  </section>

  <section class="program-ledger">
    <h2 class="program-title">"Maple Step" program</h2>
    <ul class="program-list">
      <li>Monthly ledger preparation</li>
    </ul>
  </section>

  <section class="contact">
    <p class="contact-label">CONTACT</p>
    <ul class="contact-details">
      <li>(555) 014-8270</li>
      <li>hello@tamberlyfinancing.com</li>
    </ul>
  </section>
</main>
</body>
</html>
```